Product Labels - Background and Layout Refresh - Made in Australia

We require 2 labels designs to be updated. One for our premium Ironvale brand and a second one for our standard quality Durello brand.
We also require a new cover for our 2018 product catalog. Attached is the current design. We need an industrial type image in the background. Text to remain the same, fonts and textures can be changed.
Ironvale: QX-004-7389-R+.ai
The old Corvane product has been replaced with the new Ironvale brand. Remove the corvane logo and use the attached Ironvale logo. Change background, fonts and layout. Use the made in Australia Logo or the words Made In Australia.
Durello: QX-004-7389.ai
The logo remains the same, the background and the fonts are to be changed and updated.
Use made in Australia Logo or the words Made In Australia.
The text and diagram content must all remain on the labels.
The design theme needs to stay very industrial and rough.
Made in Australia is a big selling point for our products, ensure that message is conveyed on the labels.
Note: The size of the disc is 125mm the size of the label is now 85mm
The layer "Background" is to show how the final product will look. Refer to .jpg for details.
Target Market(s)
Industrial user of tools
Industry/Entity Type
Industrial
Colors
Designer to choose colors to be used in the design.
Requirements
Must have
- Industrial Feel & Emphasis on Made in Australia, by text, logo or other Images
Nice to have
- Homeforge Logo
Should not have
- Not playful, not fun.

```html
<!DOCTYPE html>
<html lang="en">
<head>
<meta charset="utf-8">
<title>Ironvale Label Design</title>
<link rel="stylesheet" href="https://fonts.googleapis.com/css2?family=Rajdhani:wght@500;600;700&display=swap">
<style>
  :root {
    --page: #ffffff;
    --ink: #111111;
    --disc: #121212;
    --disc-mesh: #262626;
    --label: #1a1a1a;
    --orange: #f5a414;
    --orange-deep: #d98a06;
    --steel-light: #b9b9b9;
    --steel-mid: #7a7a7a;
    --steel-dark: #3a3a3a;
    --white: #ffffff;
    --muted: #cfcfcf;
    --badge: #1f8a3a;
  }
  html, body {
    margin: 0;
    padding: 0;
    width: 1200px;
    height: 624px;
    overflow: hidden;
    background: var(--page);
  }
  .sheet {
    position: relative;
    width: 1200px;
    height: 624px;
    font-family: "Rajdhani", "Arial Narrow", sans-serif;
  }
  .sheet-title {
    position: absolute;
    top: 30px;
    left: 0;
    width: 100%;
    margin: 0;
    text-align: center;
    font-size: 27px;
    font-weight: 700;
    color: var(--ink);
  }
  .artwork {
    position: absolute;
    inset: 0;
  }
  .brand-name { font-weight: 700; font-size: 31px; fill: var(--orange); letter-spacing: 0.5px; }
  .band-text { font-weight: 700; font-size: 15px; fill: #111; letter-spacing: 0.5px; }
  .line-title { font-weight: 700; font-size: 16px; fill: var(--orange); letter-spacing: 0.3px; }
  .hex-text { font-weight: 700; font-size: 17px; fill: var(--white); }
  .spec-title { font-weight: 700; font-size: 11px; fill: var(--orange); }
  .spec-small { font-weight: 600; font-size: 7px; fill: var(--white); }
  .danger { font-weight: 700; font-size: 9.5px; fill: var(--orange); }
  .speed { font-weight: 700; font-size: 8.5px; fill: var(--white); }
  .diagram-caption { font-weight: 500; font-size: 4px; fill: var(--muted); }
  .diagram-verdict { font-weight: 700; font-size: 5px; fill: var(--white); }
  .ring-text { font-weight: 600; font-size: 7.6px; fill: var(--white); letter-spacing: 0.6px; }
</style>
</head>
<body>
<main class="sheet">
  <h1 class="sheet-title">Ironvale Label Design</h1>

  <svg class="artwork" width="1200" height="624" viewBox="0 0 1200 624" xmlns="http://www.w3.org/2000/svg">
    <defs>
      <pattern id="disc-mesh" width="6" height="6" patternUnits="userSpaceOnUse">
        <rect width="6" height="6" fill="var(--disc)"/>
        <path d="M0 0H6M0 0V6" stroke="var(--disc-mesh)" stroke-width="1"/>
      </pattern>
      <linearGradient id="steel-band" x1="0" y1="0" x2="0" y2="1">
        <stop offset="0" stop-color="var(--steel-dark)"/>
        <stop offset="0.35" stop-color="var(--steel-light)"/>
        <stop offset="0.6" stop-color="var(--steel-mid)"/>
        <stop offset="1" stop-color="var(--steel-dark)"/>
      </linearGradient>
      <linearGradient id="silver-ring" x1="0" y1="0" x2="1" y2="1">
        <stop offset="0" stop-color="#f2f2f2"/>
        <stop offset="0.5" stop-color="#8a8a8a"/>
        <stop offset="1" stop-color="#e6e6e6"/>
      </linearGradient>
      <radialGradient id="back-decoration" cx="0.5" cy="0.5" r="0.5">
        <stop offset="0" stop-color="#1f1f1f"/>
        <stop offset="0.85" stop-color="#141414"/>
        <stop offset="1" stop-color="#000000"/>
      </radialGradient>
      <clipPath id="label-clip">
        <circle cx="302" cy="312" r="176"/>
      </clipPath>
      <path id="ring-outer" d="M 142 350 A 164 164 0 0 0 462 350"/>
      <path id="ring-inner" d="M 156 345 A 150 150 0 0 0 448 345"/>
    </defs>

    <!-- Front disc -->
    <g class="disc-front">
      <circle cx="302" cy="312" r="256" fill="url(#disc-mesh)"/>
      <g class="label" clip-path="url(#label-clip)">
        <circle cx="302" cy="312" r="176" fill="var(--label)"/>

        <text class="brand-name" x="306" y="198" text-anchor="middle">IRONVALE</text>

        <g class="professional-band">
          <rect x="210" y="210" width="190" height="16" fill="var(--orange)"/>
          <text class="band-text" x="305" y="223" text-anchor="middle">PROFESSIONAL</text>
        </g>
        <text class="line-title" x="305" y="243" text-anchor="middle">FABRICATION PRODUCTS</text>

        <g class="safety-icons" fill="none" stroke="var(--orange)" stroke-width="1.6">
          <circle cx="166" cy="252" r="5"/>
          <circle cx="184" cy="252" r="5"/>
          <circle cx="202" cy="252" r="5"/>
          <circle cx="404" cy="252" r="5"/>
          <circle cx="422" cy="252" r="5"/>
          <circle cx="440" cy="252" r="5"/>
        </g>

        <g class="steel-band">
          <rect x="120" y="270" width="370" height="84" fill="url(#steel-band)"/>
          <g fill="#222">
            <circle cx="140" cy="276" r="1.4"/><circle cx="180" cy="276" r="1.4"/><circle cx="220" cy="276" r="1.4"/>
            <circle cx="260" cy="276" r="1.4"/><circle cx="344" cy="276" r="1.4"/><circle cx="384" cy="276" r="1.4"/>
            <circle cx="424" cy="276" r="1.4"/><circle cx="464" cy="276" r="1.4"/>
            <circle cx="140" cy="348" r="1.4"/><circle cx="180" cy="348" r="1.4"/><circle cx="220" cy="348" r="1.4"/>
            <circle cx="260" cy="348" r="1.4"/><circle cx="344" cy="348" r="1.4"/><circle cx="384" cy="348" r="1.4"/>
            <circle cx="424" cy="348" r="1.4"/><circle cx="464" cy="348" r="1.4"/>
          </g>
        </g>

        <g class="size-badge">
          <polygon points="198,284 214,293 214,311 198,320 182,311 182,293" fill="#111" stroke="#555"/>
          <text class="hex-text" x="198" y="308" text-anchor="middle">5"</text>
        </g>
        <g class="grade-badge">
          <polygon points="414,284 430,293 430,311 414,320 398,311 398,293" fill="#111" stroke="#555"/>
          <text class="hex-text" x="414" y="308" text-anchor="middle" font-size="14">CA⁺</text>
        </g>

        <g class="spec-left">
          <text class="spec-title" x="194" y="331" text-anchor="middle">IRON FREE</text>
          <text class="spec-small" x="194" y="339" text-anchor="middle">125 x 1 x 22mm</text>
          <text class="spec-small" x="194" y="346" text-anchor="middle">Complies with AS1788</text>
        </g>
        <g class="spec-right">
          <text class="spec-title" x="414" y="331" text-anchor="middle">CUTTING DISC</text>
          <text class="spec-small" x="414" y="340" text-anchor="middle" font-size="8" font-weight="700">SKU: QX-004-7389-R+</text>
        </g>

        <text class="danger" x="302" y="377" text-anchor="middle">Danger: Do not exceed the maximum safe speed.</text>
        <text class="speed" x="302" y="390" text-anchor="middle">Max. RPM 12,250 - 80 m/s</text>

        <g class="mounting-diagrams">
          <rect x="252" y="400" width="36" height="26" fill="#2a2a2a" role="img" aria-label="Flange mounting diagram, correct fitting"/>
          <text class="diagram-caption" x="270" y="430" text-anchor="middle">Flanges equal in diameter</text>
          <text class="diagram-verdict" x="270" y="440" text-anchor="middle">CORRECT</text>
          <rect x="292" y="400" width="36" height="26" fill="#2a2a2a" role="img" aria-label="Flange mounting diagram, incorrect fitting"/>
          <text class="diagram-caption" x="310" y="430" text-anchor="middle">Flanges not equal in diameter</text>
          <text class="diagram-verdict" x="310" y="440" text-anchor="middle">INCORRECT</text>
        </g>

        <rect class="origin-badge" x="342" y="400" width="26" height="28" rx="2" fill="var(--badge)" role="img" aria-label="Homeforge origin badge"/>

        <text class="ring-text"><textPath href="#ring-inner" startOffset="50%" text-anchor="middle">Flanges must be min. 1/3 diameter of wheel. Flanges must be fitted as illustrated above.</textPath></text>
        <text class="ring-text"><textPath href="#ring-outer" startOffset="50%" text-anchor="middle">Warning: Cutting wheels must be mounted correctly. Metal guards must be used on all machines. Made in PRC</textPath></text>
      </g>
      <circle cx="302" cy="312" r="176" fill="none" stroke="url(#silver-ring)" stroke-width="5"/>
      <circle class="arbor-hole" cx="302" cy="308" r="46" fill="var(--page)"/>
    </g>

    <!-- Back disc -->
    <g class="disc-back">
      <circle cx="898" cy="312" r="256" fill="#000"/>
      <circle cx="898" cy="314" r="166" fill="url(#back-decoration)" role="img" aria-label="Faint repeating brand emblem pattern on the back of the disc"/>
    </g>
  </svg>
</main>
</body>
</html>
```